FenderPals Personal Injury Lawyers Website (Wordpress)

We need a brand new website for our firm's new rebranding. The name of the website is www.fenderpals-example.com. Our new brand will be a group of personal injury lawyers focused on representing only victims in car wrecks. We will be distinguishing ourselves from other law firms due to the fact that other law firms represent clients involving all forms of personal injury. We will only focus on car wrecks and this needs to be reflected on the website.

I have attached the new firm logo and stationary to show the designers the kind of look we are going for in the new website. It needs to be clean, pure, and show the potential clients that we only do one thing and we do it well. That thing is car wrecks.

Some examples of websites that we like are the following:
www.qvt-example.lu - nice interface and colors. nice navigation, we really like the biography pages for the individuals attorneys
www.morvantlegal-example.com - good layout, good navigation
www.pelliardwoss-example.com - navigation bar follows the user whether the user goes up or down

We would like five separate pages -- (1) Home, (2) Client Resources, (3) Expertise / Car Wrecks, (4) Contact Us, (5) News

The Home page will be used for driving traffic and should have a call to action on the right at the top stating that we will send an ebook to anyone who gives their contact information. The ebook will explain how car wrecks work. This should also have room for youtube videos which will be added later.

The client resources will include blogs, books, and information for potential clients. It should be presented in a well developed manner which is both appealing to potential and current clients.

The expertise page will show that we only focus on car wrecks. This needs to be a recurrent theme throughout the entire website. This page will focus on car wrecks and the different aspects including damages, insurance, and investigation.

The Contact Us page will show a google map to our address and phone number. Please use generic information and we will fill in the gaps upon the selection.

News: the news page will show different articles related to past and present cases and the successes of those clients.

The overall page should be elegant and creative. Do not include courthouses, gavels or anything else related to the law. If you include these things, your design will automatically be excluded.
Updates

Please take note this design is now guaranteed. I look forward to receiving everyone's wonderful designs.

Target Market(s)

Persons involved in car wrecks

Industry/Entity Type

Legal

Coding

Coded - Design and coding required

Number of Pages Required

5+ page

Font styles to use
Serif
Sans Serif

Colors
ec1f27
ffffff
000000

Requirements
Must have
• Five pages which focus on representation of car wreck victims. The site must be clean and easy to navigate.
Nice to have
• Navigation bar should follow user up and down the page.
Should not have
• Gavels, court houses, anything related to the law. If your design has these aspects, it will automatically be rejected

```html
<!DOCTYPE html>
<html lang="en">
<head>
<meta charset="utf-8">
<title>FenderPals – Personal Injury Lawyers</title>
<link rel="stylesheet" href="https://fonts.googleapis.com/css2?family=Oswald:wght@400;500;700&family=Open+Sans:wght@400;600;700&family=Roboto+Slab:wght@400;700&display=swap">
<style>
:root{
  --red:#ec1f27;
  --red-dark:#c8161d;
  --black:#000000;
  --ink:#222222;
  --text:#666666;
  --muted:#999999;
  --line:#e3e3e3;
  --white:#ffffff;
  --footer:#2a2a2a;
  --footer-deep:#1e1e1e;
  --field:#3a3a3a;
}
*{box-sizing:border-box;margin:0;padding:0}
html,body{width:1200px;height:3240px;overflow:hidden}
body{background:var(--white);font-family:'Open Sans',Arial,sans-serif;color:var(--text);font-size:13px;line-height:1.6}
.wrap{width:1008px;margin:0 auto;position:relative}

/* header */
.site-header{height:80px;border-bottom:1px solid var(--line)}
.site-header .wrap{display:flex;justify-content:space-between;align-items:center;height:80px}
.brand{display:flex;flex-direction:column}
.brand-name{font-family:'Oswald',sans-serif;font-weight:700;font-size:34px;line-height:1;color:var(--red);letter-spacing:.5px}
.brand-tag{font-family:'Open Sans',sans-serif;font-size:10px;letter-spacing:1.5px;color:var(--ink);font-weight:600;margin-top:4px}
.main-nav{display:flex;gap:4px;align-items:flex-start;height:80px;padding-top:16px}
.main-nav a{font-size:13px;color:var(--ink);text-decoration:none;padding:6px 12px}
.main-nav a.active{background:var(--red);color:var(--white)}

/* hero */
.hero{height:400px;position:relative;background:linear-gradient(135deg,#4a4e55 0%,#8b9099 35%,#c9ccd1 55%,#6d7076 80%,#3b3d42 100%)}
.hero-arrow{position:absolute;top:176px;width:32px;height:48px;background:rgba(0,0,0,.55);display:flex;align-items:center;justify-content:center}
.hero-arrow.prev{left:0}.hero-arrow.next{right:0;background:var(--red)}

/* welcome bar */
.welcome-bar{height:40px;border-bottom:1px solid var(--line)}
.welcome-bar .wrap{display:flex;align-items:center;justify-content:space-between;height:40px}
.welcome-left{display:flex;align-items:center;gap:12px;font-size:12px;color:var(--ink)}
.welcome-icon{width:24px;height:24px;background:var(--red)}
.social{display:flex;gap:6px}
.social span{width:24px;height:24px;background:#d9d9d9}
.social span.on{background:var(--red)}

/* about */
.about{height:320px;padding-top:80px}
.about .wrap{display:flex;gap:40px}
.about-title{width:480px}
.about-title h1{font-family:'Oswald',sans-serif;font-weight:700;font-size:68px;line-height:1;color:var(--black);letter-spacing:1px}
.about-title p{font-size:17px;color:var(--ink);margin-top:14px;line-height:1.5}
.hl{color:var(--red)}
.about-copy{flex:1;font-size:13px}
.about-copy p+p{margin-top:16px}

/* section headings */
.section-rule{border-top:1px solid var(--line)}
.sub-heading{font-family:'Open Sans',sans-serif;font-weight:700;font-size:20px;color:var(--ink)}
.big-heading{font-family:'Oswald',sans-serif;font-weight:700;font-size:52px;color:var(--black);text-align:center;line-height:1}

/* recent wrecks */
.wrecks{height:500px;padding-top:40px}
.wreck-grid{display:flex;gap:24px;margin-top:28px}
.wreck-card{width:320px;text-align:center}
.wreck-photo{height:180px;position:relative}
.photo-a{background:linear-gradient(135deg,#2d2f33,#6e7178 50%,#b5b8bd)}
.photo-b{background:linear-gradient(135deg,#a37a5c,#d7b597 50%,#7c5a44)}
.photo-c{background:linear-gradient(135deg,#3a3c40,#9aa0a8 50%,#55585d)}
.plus{position:absolute;left:136px;top:66px;width:48px;height:48px;border-radius:50%;background:var(--red);display:flex;align-items:center;justify-content:center}
.wreck-card h3{font-family:'Roboto Slab',serif;font-weight:400;font-size:24px;color:var(--ink);margin:22px 0 10px}
.wreck-card p{font-size:11px;line-height:1.6;padding:0 10px}

/* client resources */
.resources{height:600px;padding-top:20px}
.blog-label{margin-top:40px}
.blog-grid{display:grid;grid-template-columns:492px 492px;gap:24px;margin-top:28px}
.blog-card{height:200px;position:relative;overflow:hidden}
.blog-card .shade{position:absolute;inset:0}
.blog-card .caption{position:absolute;left:24px;top:30px;color:var(--white)}
.blog-card .caption h4{font-family:'Oswald',sans-serif;font-weight:500;font-size:30px;line-height:1.1;letter-spacing:1px}
.blog-card .caption small{display:block;font-size:11px;margin-top:8px}
.shade-1{background:linear-gradient(90deg,var(--red) 0 50%,#8d8a86 50%,#c5b8aa 100%)}
.shade-2{background:linear-gradient(135deg,#7a5b49,#caa88b 50%,#4c4a48)}
.shade-3{background:linear-gradient(135deg,#3d3f44,#a7abb1 55%,#616469)}
.shade-4{background:linear-gradient(135deg,#e8e8e8,#cfd2d5 50%,#9a3030)}
.caption.dark h4,.caption.dark small{color:var(--white)}

/* books */
.books{height:370px;background:var(--red);padding-top:24px}
.books h3{font-family:'Open Sans',sans-serif;font-weight:700;font-size:20px;color:var(--white)}
.book-row{display:flex;gap:20px;margin-top:24px;position:relative}
.book{width:151px;height:230px;background:linear-gradient(160deg,#1b1b1b,#4b4b4b 60%,#2a2a2a);position:relative;box-shadow:0 4px 10px rgba(0,0,0,.3)}
.book .band{position:absolute;top:0;left:0;right:0;height:22px;background:rgba(236,31,39,.85)}
.book .band span{position:absolute;right:8px;top:3px;font-size:10px;color:var(--white);font-weight:700}
.book .title{position:absolute;left:0;right:0;top:86px;text-align:center;font-family:'Oswald',sans-serif;font-weight:700;font-size:32px;line-height:1;color:var(--white)}
.book-arrow{position:absolute;top:100px;width:28px;height:32px;background:rgba(0,0,0,.6);display:flex;align-items:center;justify-content:center}
.book-arrow.prev{left:-12px}.book-arrow.next{right:-12px}

/* news */
.news{height:390px;padding-top:40px}
.news-intro{width:600px;margin:18px auto 0;text-align:center;font-size:12px;color:var(--muted)}
.news-grid{display:flex;gap:40px;margin-top:30px}
.news-item{width:484px;display:flex;gap:20px}
.news-photo{width:234px;height:120px;flex:none}
.news-photo.p1{background:linear-gradient(135deg,#6e5444,#c9a98f 50%,#e2d2c3)}
.news-photo.p2{background:linear-gradient(135deg,#d8d8d8,#b03a3a 50%,#f0f0f0)}
.news-item h4{font-family:'Open Sans',sans-serif;font-weight:700;font-size:14px;color:var(--ink);line-height:1.3}
.news-item p{font-size:11px;margin-top:6px;line-height:1.5}
.btn{display:inline-block;background:var(--red);color:var(--white);font-size:11px;font-weight:700;padding:6px 18px;margin-top:10px}

/* footer */
.site-footer{height:480px;background:var(--footer);color:#bbbbbb;padding-top:44px;position:relative}
.foot-cols{display:flex;gap:36px}
.foot-col{width:224px;font-size:11px;line-height:1.7}
.foot-col h5{font-family:'Open Sans',sans-serif;font-weight:700;font-size:20px;color:var(--white);margin-bottom:22px}
.foot-col p+p{margin-top:12px}
.links li{list-style:none;padding-left:14px;position:relative;margin-bottom:8px}
.links li::before{content:"";position:absolute;left:0;top:8px;width:5px;height:5px;background:var(--red)}
.tweet{display:flex;gap:10px;margin-bottom:14px}
.tweet i{width:14px;height:14px;border-radius:50%;background:var(--red);flex:none;margin-top:3px}
.field{height:30px;background:var(--field);border:1px solid #4a4a4a;margin-bottom:8px;padding:6px 10px;color:var(--muted)}
.field.area{height:70px}
.submit{display:inline-block;background:var(--red);color:var(--white);font-weight:700;padding:8px 30px;font-size:12px;margin-top:4px}
.foot-bottom{position:absolute;left:0;right:0;bottom:0;height:44px;background:var(--footer-deep);font-size:11px;color:var(--muted)}
.foot-bottom .wrap{line-height:44px}
</style>
</head>
<body>

<header class="site-header">
  <div class="wrap">
    <div class="brand">
      <span class="brand-name">FenderPals</span>
      <span class="brand-tag">PERSONAL INJURY LAWYERS</span>
    </div>
    <nav class="main-nav">
      <a class="active">Home</a><a>Car Wrecks</a><a>Client Resources</a><a>Expertise</a><a>Contact Us</a><a>News</a>
    </nav>
  </div>
</header>

<section class="hero" role="img" aria-label="Slideshow photo of an overturned car at a crash scene with an ambulance and paramedic">
  <span class="hero-arrow prev"><svg width="12" height="18" viewBox="0 0 12 18"><path d="M9 2 2 9l7 7" stroke="#fff" stroke-width="2.5" fill="none"/></svg></span>
  <span class="hero-arrow next"><svg width="12" height="18" viewBox="0 0 12 18"><path d="M3 2l7 7-7 7" stroke="#fff" stroke-width="2.5" fill="none"/></svg></span>
</section>

<div class="welcome-bar">
  <div class="wrap">
    <div class="welcome-left"><span class="welcome-icon"></span>Welcome To FenderPals</div>
    <div class="social"><span></span><span></span><span class="on"></span><span class="on"></span></div>
  </div>
</div>

<section class="about">
  <div class="wrap">
    <div class="about-title">
      <h1>ABOUT US</h1>
      <p>Lorem Ipsum is simply dummy text of the printing <br>and <strong class="hl">typesetting industry.</strong></p>
    </div>
    <div class="about-copy">
      <p>Contrary to popular belief, Lorem Ipsum is not simply random text. It has roots in a piece of classical Latin literature from 45 BC, making it over <span class="hl">2000 years old. Darren Holloway</span>.</p>
      <p>This book is a treatise on the theory of ethics, very popular during the Renaissance. The first line of Lorem Ipsum, <span class="hl">"Lorem ipsum dolor sit amet.."</span>, comes from a line in section 1.10.32.</p>
    </div>
  </div>
</section>

<section class="wrecks section-rule">
  <div class="wrap">
    <h2 class="sub-heading">RECENT CAR WRECKS</h2>
    <div class="wreck-grid">
      <article class="wreck-card">
        <div class="wreck-photo photo-a" role="img" aria-label="Photo of a car with a crushed front end"></div>
        <h3>Car Damages</h3>
        <p>Contrary to popular belief, Lorem Ipsum is not simply random text. It has roots in a piece of classical Latin literature from 45 BC, made over 2000 years old. Darren Holloway, a Latin professor at Ashcombe College in Virginia.</p>
      </article>
      <article class="wreck-card">
        <div class="wreck-photo photo-b" role="img" aria-label="Photo of a driver calling for help after a collision">
          <span class="plus"><svg width="20" height="20" viewBox="0 0 20 20"><path d="M10 2v16M2 10h16" stroke="#fff" stroke-width="3"/></svg></span>
        </div>
        <h3>Car Insurances</h3>
        <p>Contrary to popular belief, Lorem Ipsum is not simply random text. It has roots in a piece of classical Latin literature from 45 BC, made over 2000 years old. Darren Holloway, a Latin professor at Ashcombe College in Virginia.</p>
      </article>
      <article class="wreck-card">
        <div class="wreck-photo photo-c" role="img" aria-label="Photo of a wrecked car being inspected at the roadside"></div>
        <h3>Car Investigation</h3>
        <p>Contrary to popular belief, Lorem Ipsum is not simply random text. It has roots in a piece of classical Latin literature from 45 BC, made over 2000 years old. Darren Holloway, a Latin professor at Ashcombe College in Virginia.</p>
      </article>
    </div>
  </div>
</section>

<section class="resources">
  <div class="wrap">
    <h2 class="big-heading">CLIENT RESOURCES</h2>
    <h3 class="sub-heading blog-label">Latest From The Blog</h3>
    <div class="blog-grid">
      <article class="blog-card"><div class="shade shade-1" role="img" aria-label="Photo of a damaged car beside a red caption panel"></div>
        <div class="caption"><h4>VESTIBULUM<br>LIBERONISL.</h4><small>Lorem ipsum dolor sit amet consectetur</small></div></article>
      <article class="blog-card"><div class="shade shade-2" role="img" aria-label="Photo of a driver reporting an accident by phone"></div>
        <div class="caption dark"><h4>VESTIBULUM<br>LIBERONISL.</h4><small>Lorem ipsum dolor sit amet consectetur</small></div></article>
      <article class="blog-card"><div class="shade shade-3" role="img" aria-label="Photo of a car interior after a crash"></div>
        <div class="caption dark"><h4>VESTIBULUM<br>LIBERONISL.</h4><small>Lorem ipsum dolor sit amet consectetur</small></div></article>
      <article class="blog-card"><div class="shade shade-4" role="img" aria-label="Photo of a warning triangle on the road behind a stopped car"></div>
        <div class="caption dark"><h4>VESTIBULUM<br>LIBERONISL.</h4><small>Lorem ipsum dolor sit amet consectetur</small></div></article>
    </div>
  </div>
</section>

<section class="books">
  <div class="wrap">
    <h3>Books</h3>
    <div class="book-row">
      <div class="book" role="img" aria-label="Book cover: Car Wrecks, volume 1"><div class="band"><span>VOL 1</span></div><div class="title">CAR<br>WRECKS</div></div>
      <div class="book" role="img" aria-label="Book cover: Car Wrecks, volume 2"><div class="band"><span>VOL 2</span></div><div class="title">CAR<br>WRECKS</div></div>
      <div class="book" role="img" aria-label="Book cover: Car Wrecks, volume 3"><div class="band"><span>VOL 3</span></div><div class="title">CAR<br>WRECKS</div></div>
      <div class="book" role="img" aria-label="Book cover: Car Wrecks, volume 4"><div class="band"><span>VOL 4</span></div><div class="title">CAR<br>WRECKS</div></div>
      <div class="book" role="img" aria-label="Book cover: Car Wrecks, volume 5"><div class="band"><span>VOL 5</span></div><div class="title">CAR<br>WRECKS</div></div>
      <div class="book" role="img" aria-label="Book cover: Car Wrecks, volume 6"><div class="band"><span>VOL 6</span></div><div class="title">CAR<br>WRECKS</div></div>
      <span class="book-arrow prev"><svg width="10" height="16" viewBox="0 0 10 16"><path d="M8 2 2 8l6 6" stroke="#fff" stroke-width="2" fill="none"/></svg></span>
      <span class="book-arrow next"><svg width="10" height="16" viewBox="0 0 10 16"><path d="M2 2l6 6-6 6" stroke="#fff" stroke-width="2" fill="none"/></svg></span>
    </div>
  </div>
</section>

<section class="news">
  <div class="wrap">
    <h2 class="big-heading">LATEST NEWS</h2>
    <p class="news-intro">Mauris accumsan eros eget libero posuere vulputate. Etiam elit elit, elementum sed varius at, lacinia vitae nisl, ultricies sapien.</p>
    <div class="news-grid">
      <article class="news-item">
        <div class="news-photo p1" role="img" aria-label="Photo of a family standing beside their car"></div>
        <div><h4>We know your home is important to you</h4>
          <p>Lorem ipsum dolor sit amet, consectetur adipiscing elit. Sed dictum lacus vitae nibh tempus cursus.</p>
          <span class="btn">READ MORE</span></div>
      </article>
      <article class="news-item">
        <div class="news-photo p2" role="img" aria-label="Photo of a red warning triangle placed on the road"></div>
        <div><h4>Premier Commercial Roofing Company</h4>
          <p>Lorem ipsum dolor sit amet, consectetur adipiscing elit. Sed dictum lacus vitae nibh tempus cursus.</p>
          <span class="btn">READ MORE</span></div>
      </article>
    </div>
  </div>
</section>

<footer class="site-footer">
  <div class="wrap foot-cols">
    <div class="foot-col">
      <h5>Contact</h5>
      <p>FenderPals</p>
      <p>Larkfield Office / Head Office<br>Level 3, Suite 210, 17 Orchard Street<br>Larkfield, NV 80123<br>Phone: (555) 014-2290</p>
      <p>Brookvale Office<br>Shop 4, 88 Harbour Road<br>Brookvale, NV 80145<br>(555) 014-3371</p>
    </div>
    <div class="foot-col">
      <h5>Quick Links</h5>
      <ul class="links">
        <li>Lorem ipsum dolor sit</li><li>Nulla consequat</li><li>Praesent vel nunc id</li><li>Curabitur hendrerit</li><li>Aliquam eget massa</li><li>Cras id turpis eros</li><li>Fusce nec justo</li>
      </ul>
    </div>
    <div class="foot-col">
      <h5>Latest Tweets</h5>
      <div class="tweet"><i></i><span>@fenderpals Lorem ipsum dolor sit amet consectetur, sed do eiusmod tempor incididunt ut labore et dolore. 1 day ago</span></div>
      <div class="tweet"><i></i><span>@fenderpals Ut enim ad minim veniam, quis nostrud exercitation ullamco laboris nisi ut aliquip ex ea. 2 days ago</span></div>
      <div class="tweet"><i></i><span>@fenderpals Duis aute irure dolor in reprehenderit in voluptate velit esse cillum dolore. 3 days ago</span></div>
    </div>
    <div class="foot-col">
      <h5>Contact Us</h5>
      <div class="field">First Name</div>
      <div class="field">Last Name</div>
      <div class="field">Subject</div>
      <div class="field area">Message</div>
      <span class="submit">Submit</span>
    </div>
  </div>
  <div class="foot-bottom"><div class="wrap">Copyright © 2014 FenderPals. All Rights Reserved.</div></div>
</footer>

</body>
</html>
```